Something that stands out and has more of a modern look to it...will be printing on plastic cards so keep in mind and review old business card as reference

Industry/Entity Type

Real Estate Agent

Contact Information for Business Card

Front of business card will have picture and information the back of card can have logo or name in cursive etc

Logo Text

Marcus Belvane

Font styles to use
Decorative
Script

Colors

Designer to choose colors to be used in the design.

Requirements
Must have
• Must have "Summit 84" logo and state "Clearwater Realty Inc Brokerage*" next to it.
• Offices in: Toronto, Markham, Durham
• *Independently Owned and Operated trademarks owned by Summit 84 Real Estate LLC used under license or authorized sub-license. 2017 Summit 84 Canada Limited Partnership. (See old business card for reference)
• Email address: marcus@mbelvanehomes.example
• Website: www.MBelvaneHomes.example
• Direct: 647-555-0184
• Name: Marcus Bel Vane
• Office: 905-555-0139
Nice to have
• Maybe a catchy slogan
• One side can have my name designed or the Logo
Should not have
• The Summit 84 Logo too large or focused on (my business requires me just to have this somewhere on the card).
• Yellow and black theme

```html
<!DOCTYPE html>
<html lang="en">
<head>
<meta charset="utf-8">
<title>Marcus Bel Vane – Business Card</title>
<link href="https://fonts.googleapis.com/css2?family=Lato:wght@400;700;900&family=Roboto+Condensed:wght@400&display=swap" rel="stylesheet">
<style>
  :root {
    --stage: #2e2e2e;
    --deep: #13233f;
    --paper: #ffffff;
    --accent: #3f8fc9;
    --navy: #1f3f86;
    --text: #141414;
  }
  * { box-sizing: border-box; margin: 0; padding: 0; }
  html, body { width: 1200px; height: 900px; overflow: hidden; }
  body { background: var(--stage); font-family: "Lato", sans-serif; position: relative; }

  .card { position: absolute; left: 220px; width: 760px; height: 434px; overflow: hidden; }

  /* Back side */
  .card-back { top: 12px; background: var(--deep); color: var(--paper); text-align: center; }
  .card-back .monogram {
    position: absolute; left: 250px; top: 70px; width: 260px; height: 100px;
    background: linear-gradient(90deg, rgba(63,143,201,0.15), rgba(63,143,201,0.5), rgba(63,143,201,0.15));
    border-radius: 50px;
  }
  .card-back .brand-name {
    position: absolute; left: 0; right: 0; top: 184px;
    font-size: 46px; font-weight: 400; letter-spacing: 3px; text-transform: uppercase;
  }
  .card-back .website { position: absolute; left: 0; right: 0; top: 330px; font-size: 19px; letter-spacing: 0.5px; }

  /* Front side */
  .card-front { top: 466px; background: var(--paper); color: var(--text); }
  .card-front .portrait {
    position: absolute; left: 30px; top: 36px; width: 250px; height: 398px;
    border-radius: 110px 110px 0 0;
    background: linear-gradient(180deg, #c9957a 0%, #b98a72 38%, #e9e6e2 52%, var(--navy) 64%, #1a326b 100%);
  }
  .card-front .swoosh { position: absolute; inset: 0; width: 760px; height: 434px; }
  .card-front .website { position: absolute; left: 28px; top: 398px; color: var(--paper); font-size: 19px; }

  .agent-name { position: absolute; right: 26px; top: 52px; font-size: 36px; font-weight: 900; letter-spacing: 1px; text-transform: uppercase; }
  .rule { position: absolute; left: 330px; right: 26px; top: 104px; height: 2px; background: var(--accent); }
  .agent-title { position: absolute; right: 26px; top: 110px; color: var(--accent); font-size: 21px; }
  .brokerage { position: absolute; left: 298px; top: 162px; font-size: 19px; }
  .network-mark { position: absolute; right: 26px; top: 152px; display: flex; align-items: center; gap: 6px; font-size: 26px; font-weight: 900; }
  .network-mark .dot { width: 14px; height: 14px; background: var(--accent); }
  .offices { position: absolute; right: 26px; top: 204px; font-size: 22px; }
  .disclaimer {
    position: absolute; right: 26px; top: 236px; width: 440px; text-align: right;
    font-family: "Roboto Condensed", sans-serif; font-size: 14px; line-height: 1.25;
  }
  .contacts { position: absolute; right: 26px; top: 298px; list-style: none; text-align: right; }
  .contacts li { display: flex; justify-content: flex-end; align-items: center; gap: 12px; font-size: 22px; line-height: 30px; }
  .contacts svg { width: 20px; height: 20px; fill: var(--accent); }
</style>
</head>
<body>

<section class="card card-back">
  <div class="monogram" role="img" aria-label="Script monogram of the agent's initials"></div>
  <h1 class="brand-name">Marcus Bel Vane</h1>
  <p class="website">www.MBelvaneHomes.example</p>
</section>

<section class="card card-front">
  <div class="portrait" role="img" aria-label="Portrait of the agent in a navy blazer and white shirt"></div>
  <svg class="swoosh" viewBox="0 0 760 434" aria-hidden="true">
    <path d="M250 384 C420 398 600 412 760 420 L760 430 C600 424 420 410 250 390 Z" fill="var(--accent)"/>
    <path d="M0 384 C150 386 290 398 400 434 L0 434 Z" fill="var(--deep)"/>
  </svg>
  <p class="website">www.MBelvaneHomes.example</p>

  <h2 class="agent-name">Marcus Bel Vane</h2>
  <div class="rule"></div>
  <p class="agent-title">Sales Representative</p>
  <p class="brokerage">Clearwater Realty Inc Brokerage</p>
  <div class="network-mark"><span class="dot"></span>Summit 84</div>
  <p class="offices">Toronto, Markham, Durham</p>
  <p class="disclaimer">Independently Owned and Operated trademarks owned by Summit 84 Real Estate LLC used under license or authorized sub-license. 2017 Summit 84 Canada Limited Partnership</p>
  <ul class="contacts">
    <li>905-555-0139 (Office)
      <svg viewBox="0 0 24 24"><path d="M6.6 10.8a15 15 0 0 0 6.6 6.6l2.2-2.2a1 1 0 0 1 1-.25 11.4 11.4 0 0 0 3.6.57 1 1 0 0 1 1 1V20a1 1 0 0 1-1 1A17 17 0 0 1 3 4a1 1 0 0 1 1-1h3.5a1 1 0 0 1 1 1c0 1.25.2 2.45.57 3.57a1 1 0 0 1-.25 1z"/></svg></li>
    <li>647-555-0184 (Direct)
      <svg viewBox="0 0 24 24"><path d="M7 3h10v5H7zM4 9h16a2 2 0 0 1 2 2v6h-4v4H6v-4H2v-6a2 2 0 0 1 2-2zm4 7v3h8v-3z"/></svg></li>
    <li>marcus@mbelvanehomes.example
      <svg viewBox="0 0 24 24"><path d="M2 5h20v14H2zm2 2v.5l8 5 8-5V7zm0 3v7h16v-7l-8 5z"/></svg></li>
  </ul>
</section>

</body>
</html>
```